New italian pizza restaurant in Australia, looking for a clean and crisp new take away leaflet de...

We require a leaflet for a take away menu / introduction to the area for our new italian pizza restaurant. AS we are a brand new business we need to get the word out about opening and specials as well as a takeaway menu. I have attached logo and menu items along with a basic design concept to help speed up the process.

Target Market(s)

Widest age range possible, families

Colors

Designer to choose colors to be used in the design.

```html
<!DOCTYPE html>
<html lang="en">
<head>
<meta charset="utf-8">
<title>Tarrawin Pizzeria – Takeaway Menu</title>
<link rel="stylesheet" href="https://fonts.googleapis.com/css2?family=Bebas+Neue&family=Open+Sans:wght@400;600&display=swap">
<style>
  :root{
    --green:#3b8b4f;
    --green-text:#62b84a;
    --red:#e9442a;
    --red-text:#ff4f31;
    --board:#1b1d1e;
    --board-light:#2a2d2f;
    --white:#ffffff;
    --ink:#222222;
    --page:#e4e5e7;
  }
  *{box-sizing:border-box;margin:0;padding:0}
  html,body{width:881px;height:1200px;overflow:hidden;background:var(--page)}
  body{position:relative;font-family:"Open Sans",sans-serif;color:var(--white)}
  .panel{position:absolute;left:55px;width:770px;height:584px;overflow:hidden;
    background:radial-gradient(ellipse at 45% 40%,var(--board-light),var(--board) 70%);
    box-shadow:0 6px 14px rgba(0,0,0,.25)}
  .panel--outside{top:8px}
  .panel--inside{top:604px}
  .panel::before,.panel::after{content:"";position:absolute;left:0;right:0;height:22px;background:var(--green);z-index:2}
  .panel::before{top:0;border-bottom:4px solid var(--red)}
  .panel::after{bottom:0;border-top:4px solid var(--red)}
  .abs{position:absolute}
  .bar{position:absolute;height:32px;font-family:"Bebas Neue",sans-serif;font-size:29px;line-height:34px;text-align:center;color:var(--white);letter-spacing:.5px;
    clip-path:polygon(2% 8%,99% 0,100% 60%,97% 100%,1% 92%,0 40%)}
  .bar--green{background:var(--green)}
  .bar--red{background:var(--red)}
  .item-name{font-size:11.5px;line-height:14px;color:var(--green-text)}
  .item-name--red{color:var(--red-text)}
  .desc{font-size:7.6px;line-height:9.5px}
  .row{display:flex;align-items:baseline}
  .row .lead{flex:1;border-bottom:1px dotted rgba(255,255,255,.8);margin:0 2px;transform:translateY(-2px)}
  .price{font-size:7.6px}
  .menu-item{margin-bottom:3px}
  .plain-list{font-size:12px;line-height:16px}
  .plain-list .price{font-size:8px}
  .sides-title{font-size:16px;color:var(--red-text);text-align:center;margin-bottom:2px}

  /* combo */
  .combo-box{left:269px;top:172px;width:229px;height:224px;background:var(--white);border-radius:8px;color:var(--ink);text-align:center;padding-top:24px}
  .combo-line{font-size:11.5px;line-height:16px}
  .combo-price{display:inline-block;margin:6px 0 8px;width:54px;height:26px;border-radius:13px;background:var(--green);border:1.5px solid var(--red);color:var(--white);font-size:11.5px;line-height:23px}

  /* delivery */
  .delivery{left:270px;width:226px;text-align:center}
  .delivery-title{font-size:26px;font-weight:600;line-height:30px}
  .delivery-title span{color:var(--red-text)}
  .delivery-areas{font-size:12.5px;line-height:18px;color:var(--green-text)}

  /* contact */
  .contact{left:511px;width:259px;text-align:center}
  .address{font-size:11.5px;line-height:15px}
  .phone{font-family:"Bebas Neue",sans-serif;font-size:30px;line-height:34px;display:flex;justify-content:center;align-items:center;gap:6px;margin-top:6px}
  .brand-mark{left:542px;top:128px;width:200px;height:200px;border-radius:50%;background:#242729;border:3px solid var(--green)}
  .brand-name{left:511px;top:212px;width:262px;text-align:center;font-size:18px;line-height:22px;font-weight:600;letter-spacing:1px}
  .photo{background:linear-gradient(135deg,#c98a3c,#e0b35a 40%,#b9462a 75%,#5a2a18)}
  .order-bar{left:510px;top:524px;width:260px;height:38px;background:var(--red);font-size:12px;line-height:38px;text-align:center;font-weight:600}

  /* pizza tables */
  .size-head{font-size:6.5px;letter-spacing:.2px}
  .pizza-row{display:grid;align-items:end}
  .pizza-col-a .pizza-row{grid-template-columns:140px 28px 28px 28px}
  .pizza-col-b .pizza-row{grid-template-columns:144px 28px 28px 28px}
  .pizza-row .price{text-align:center}
  .special-box{left:255px;top:343px;width:255px;height:95px;background:var(--red);padding:8px 0 0 18px}
  .special-box .item-name{color:var(--white)}
  .special-box .menu-item{margin-bottom:8px}
  .meals-note{font-size:9.5px;color:var(--red-text);text-align:center}
  .pasta-title{font-size:15.5px;line-height:20px;color:var(--red-text);text-align:center}
</style>
</head>
<body>

<!-- Outside -->
<section class="panel panel--outside">
  <div class="bar bar--green" style="left:38px;top:36px;width:197px">Salads</div>
  <div class="abs" style="left:26px;top:85px;width:219px">
    <div class="menu-item"><div class="item-name">Greek Salad</div>
      <div class="desc">cos lettuce, tomato, onion, cucumber,</div>
      <div class="row desc">olives, feta cheese &amp; dressing<span class="lead"></span><span class="price">$14.5</span></div></div>
    <div class="menu-item"><div class="item-name">Grilled Chicken Salad</div>
      <div class="desc">Seasoned chicken, mixed leaves, cherry</div>
      <div class="desc">tomato, Spanish onion, cucumber with</div>
      <div class="row desc">garlic infused olive oil<span class="lead"></span><span class="price">$15.5</span></div></div>
    <div class="menu-item"><div class="item-name">Chicken Ceasar Salad</div>
      <div class="desc">Chicken, cos lettuce, croutons, shaved</div>
      <div class="desc">parmesan, anchovies, egg, bacon</div>
      <div class="row desc">served with ceaser dressing<span class="lead"></span><span class="price">$15.5</span></div></div>
  </div>
  <div class="abs plain-list" style="left:26px;top:241px;width:219px">
    <div class="sides-title">SIDES</div>
    <div class="row">Garlic Bread<span class="lead"></span><span class="price">$4.5</span></div>
    <div class="row">Chips<span class="lead"></span><span class="price">$7.5</span></div>
    <div class="row">Garden Salad<span class="lead"></span><span class="price">$5</span></div>
  </div>
  <div class="bar bar--red" style="left:35px;top:321px;width:200px">Kids</div>
  <div class="abs plain-list" style="left:26px;top:362px;width:219px">
    <div>Pasta Bolognese</div><div>Pasta Napoli</div><div>Chicken Nuggets &amp; Chips</div><div>Cheeseburger &amp; Chips</div>
  </div>
  <div class="bar bar--green" style="left:27px;top:442px;width:200px">Desserts</div>
  <div class="abs plain-list" style="left:26px;top:492px;width:209px">
    <div class="row">Gelati 500mls Varieties<span class="lead"></span><span class="price">$6.5</span></div>
    <div class="row">Baci<span class="lead"></span><span class="price">$6</span></div>
    <div class="row">Tartufo<span class="lead"></span><span class="price">$6</span></div>
    <div class="row">Chocolate Mousse<span class="lead"></span><span class="price">$6</span></div>
  </div>

  <div class="bar bar--green" style="left:288px;top:35px;width:200px">Drinks</div>
  <div class="abs plain-list" style="left:288px;top:85px;width:196px">
    <div class="row">Soft drinks 375ml<span class="lead"></span><span class="price">$2.5</span></div>
    <div class="row">Soft drinks 1.25L<span class="lead"></span><span class="price">$4.5</span></div>
    <div class="row">Water 600ml<span class="lead"></span><span class="price">$2.5</span></div>
  </div>
  <div class="abs combo-box">
    <div class="combo-line">Any 2 Family pizzas, garlic bread</div>
    <div class="combo-line">and 1.25l soft drink</div>
    <div class="combo-price">$41.00</div>
    <div class="combo-line">1 Large pizza, 1 pasta, garlic bread</div>
    <div class="combo-line">and 1.25l soft drink</div>
    <div class="combo-price">$38.00</div>
    <div class="combo-line">2 Large pizzas, 1 garlic bread</div>
    <div class="combo-line">and 1.25l soft drin</div>
    <div class="combo-price">$36.00</div>
  </div>
  <div class="bar bar--red" style="left:286px;top:154px;width:197px;z-index:1">Combo Deals!</div>
  <svg class="abs" style="left:357px;top:416px" width="57" height="44" viewBox="0 0 57 44" fill="none" stroke="#fff" stroke-width="2.2" aria-hidden="true">
    <rect x="4" y="4" width="18" height="16" rx="1"/>
    <path d="M6 30 h30 l6 -14 h6 M42 8 h8"/>
    <circle cx="12" cy="36" r="5"/><circle cx="46" cy="36" r="5"/>
    <path d="M22 26 h14 M36 16 l8 14"/>
  </svg>
  <div class="abs delivery" style="top:476px">
    <div class="delivery-title">FREE <span>DELIVERY</span></div>
    <div class="delivery-areas">to Tarrawin, Kellan Park,<br>Merridale, Oakfern<br>and Brisby</div>
  </div>

  <div class="abs contact" style="top:37px">
    <div class="address">12 Wattle Bend Dr,<br>Tarrawin 3999</div>
    <div class="phone">
      <svg width="18" height="18" viewBox="0 0 24 24" fill="#fff" aria-hidden="true"><path d="M6.6 10.8a15 15 0 0 0 6.6 6.6l2.2-2.2a1 1 0 0 1 1-.25 11.4 11.4 0 0 0 3.6.6 1 1 0 0 1 1 1V20a1 1 0 0 1-1 1A17 17 0 0 1 3 4a1 1 0 0 1 1-1h3.5a1 1 0 0 1 1 1c0 1.25.2 2.45.6 3.6a1 1 0 0 1-.25 1z"/></svg>
      900 111 222
    </div>
  </div>
  <div class="abs brand-mark" aria-hidden="true"></div>
  <div class="abs brand-name">TARRAWIN PIZZERIA</div>
  <div class="abs photo" role="img" aria-label="Photo of a cheesy pepperoni and mushroom pizza" style="left:523px;top:391px;width:247px;height:133px;border-radius:40px 0 0 0"></div>
  <div class="abs order-bar">Website/ Online ordering:</div>
</section>

<!-- Inside -->
<section class="panel panel--inside">
  <div class="bar bar--red" style="left:38px;top:33px;width:197px">Pizza</div>
  <div class="abs pizza-col-a" style="left:23px;top:88px;width:224px">
    <div class="pizza-row size-head"><span></span><span class="price">SMALL</span><span class="price">LARGE</span><span class="price">FAMILY</span></div>
    <div class="menu-item"><div class="item-name item-name--red">Capricciosa</div><div class="pizza-row desc"><span>tomato, cheese, ham,<br>mushrooms, olives</span><span class="price">$9</span><span class="price">$15</span><span class="price">$18</span></div></div>
    <div class="menu-item"><div class="item-name item-name--red">Napoli</div><div class="pizza-row desc"><span>tomato, cheese, olives, anchovies</span><span class="price">$9</span><span class="price">$15</span><span class="price">$18</span></div></div>
    <div class="menu-item"><div class="item-name item-name--red">American</div><div class="pizza-row desc"><span>tomato, cheese, salami</span><span class="price">$9</span><span class="price">$15</span><span class="price">$18</span></div></div>
    <div class="menu-item"><div class="item-name item-name--red">Vegetarian</div><div class="pizza-row desc"><span>tomato, cheese, mushroom,<br>onions, capsicum, olives</span><span class="price">$9</span><span class="price">$15</span><span class="price">$18</span></div></div>
    <div class="menu-item"><div class="item-name item-name--red">Seafood</div><div class="pizza-row desc"><span>tomato, cheese, prawns, clams,<br>anchovies</span><span class="price">$9.5</span><span class="price">$15.5</span><span class="price">$19</span></div></div>
    <div class="menu-item"><div class="item-name item-name--red">The Hot One</div><div class="pizza-row desc"><span>tomato, cheese, ham, salami, chilli</span><span class="price">$9</span><span class="price">$15</span><span class="price">$18</span></div></div>
    <div class="menu-item"><div class="item-name item-name--red">Margherita</div><div class="pizza-row desc"><span>tomato, cheese, oregano</span><span class="price">$8.5</span><span class="price">$14.5</span><span class="price">$17</span></div></div>
    <div class="menu-item"><div class="item-name item-name--red">The Lot</div><div class="pizza-row desc"><span>tomato, cheese, ham, salami,<br>bacon, mushroom, onions,<br>capsicum, pineapple, olives</span><span class="price">$10</span><span class="price">$16</span><span class="price">$19</span></div></div>
    <div class="menu-item"><div class="item-name item-name--red">Mexican</div><div class="pizza-row desc"><span>tomato, cheese, salami,<br>capsicum, chilli</span><span class="price">$9</span><span class="price">$15</span><span class="price">$18</span></div></div>
    <div class="menu-item"><div class="item-name item-name--red">Chicken</div><div class="pizza-row desc"><span>tomato, cheese, chicken, BBQ sauce</span><span class="price">$9</span><span class="price">$15</span><span class="price">$18</span></div></div>
  </div>

  <div class="bar bar--red" style="left:279px;top:33px;width:201px">Pizza</div>
  <div class="abs pizza-col-b" style="left:273px;top:88px;width:228px">
    <div class="pizza-row size-head"><span></span><span class="price">SMALL</span><span class="price">LARGE</span><span class="price">FAMILY</span></div>
    <div class="menu-item"><div class="item-name item-name--red">Meat Lovers</div><div class="pizza-row desc"><span>tomato, cheese, ham, salami,<br>bacon, BBQ sauce</span><span class="price">$10</span><span class="price">$16</span><span class="price">$19</span></div></div>
    <div class="menu-item"><div class="item-name item-name--red">The House Pizza</div><div class="pizza-row desc"><span>tomato, cheese, ham,<br>mushroom, capsicum</span><span class="price">$9</span><span class="price">$15</span><span class="price">$18</span></div></div>
    <div class="menu-item"><div class="item-name item-name--red">Ceaser's Pizza</div><div class="pizza-row desc"><span>tomato, cheese, ham, mushroom,<br>pineapple, prawns</span><span class="price">$10</span><span class="price">$16</span><span class="price">$19</span></div></div>
    <div class="menu-item"><div class="item-name item-name--red">The Breakie Pizza</div><div class="pizza-row desc"><span>tomato, cheese, bacon, egg</span><span class="price">$9</span><span class="price">$15</span><span class="price">$18</span></div></div>
    <div class="menu-item"><div class="item-name item-name--red">The Footy Special</div><div class="pizza-row desc"><span>tomato, cheese, ham, capsicum,<br>onions, pineapple</span><span class="price">$9</span><span class="price">$15</span><span class="price">$18</span></div></div>
    <div class="menu-item"><div class="item-name item-name--red">Garlic</div><div class="pizza-row desc"><span>garlic, cheese, oregano</span><span class="price">$8.5</span><span class="price">$14.5</span><span class="price">$17</span></div></div>
    <div class="menu-item"><div class="item-name item-name--red">Ham</div><div class="pizza-row desc"><span>tomato, cheese, ham</span><span class="price">$8.5</span><span class="price">$14.5</span><span class="price">$17</span></div></div>
  </div>
  <div class="abs special-box pizza-col-b">
    <div class="menu-item"><div class="item-name">The Tarrawin</div><div class="pizza-row desc"><span>tomato, cheese ham, mushrooms,<br>onions, olives</span><span class="price">$9</span><span class="price">$15</span><span class="price">$18</span></div></div>
    <div class="menu-item"><div class="item-name">The Tarra Special</div><div class="pizza-row desc"><span>tomato, cheese, ham, onions,<br>bacon, egg</span><span class="price">$10</span><span class="price">$16</span><span class="price">$19</span></div></div>
  </div>
  <div class="abs photo" role="img" aria-label="Photo of a sliced pizza with tomatoes, garlic and a glass of beer on a dark table" style="left:93px;top:453px;width:343px;height:109px;background:linear-gradient(90deg,#1f2326,#7a3a22 30%,#d29a4a 50%,#8a3a22 70%,#2a2e31)"></div>

  <div class="bar bar--green" style="left:539px;top:33px;width:200px">Main Meals</div>
  <div class="abs" style="left:524px;top:74px;width:226px">
    <div class="meals-note" style="margin-bottom:5px">(all mains served with chips or salad)</div>
    <div class="menu-item"><div class="row"><span class="item-name">Scotch Fillet Steak 300g</span><span class="lead"></span><span class="price">$25</span></div><div class="desc">grass fed, with your choice of Mushroom,<br>Pepper or Garlic sauce</div></div>
    <div class="menu-item"><div class="row"><span class="item-name">Calamari</span><span class="lead"></span><span class="price">$19.5</span></div><div class="desc">Flash fried or crumbed squid with aioli</div></div>
    <div class="menu-item"><div class="row"><span class="item-name">Chicken Parmigiana</span><span class="lead"></span><span class="price">$19.5</span></div><div class="desc">Schnitzel topped with ham, Napoli sauce &amp; mozzarella</div></div>
    <div class="menu-item"><div class="row"><span class="item-name">Veal Scallopini</span><span class="lead"></span><span class="price">$19.5</span></div><div class="desc">with your choice of mushroom or<br>creamy avocado sauce</div></div>
    <div class="menu-item"><div class="row"><span class="item-name">Veal Parmigiana</span><span class="lead"></span><span class="price">$19.5</span></div><div class="desc">schnitzel topped ham, Napoli sauce &amp; mozzarella</div></div>
  </div>
  <div class="abs pasta-title" style="left:511px;top:271px;width:259px">Pasta- Spaghetti, Penne,<br>Gnocchi, Fettucine, Linguine</div>
  <div class="abs" style="left:524px;top:318px;width:226px">
    <div class="menu-item"><div class="item-name">Bolognese</div><div class="row desc">traditional Italian meat sauce<span class="lead"></span><span class="price">$14</span></div></div>
    <div class="menu-item"><div class="item-name">Carbonara</div><div class="row desc">onion, bacon, egg in creamy parmesan cheese sauce<span class="lead"></span><span class="price">$14</span></div></div>
    <div class="menu-item"><div class="item-name">Napolitana</div><div class="row desc">traditional Italian Napoli sauce<span class="lead"></span><span class="price">$13.5</span></div></div>
    <div class="menu-item"><div class="item-name">Amatriciana</div><div class="desc">bacon, onion, olives, capsicum, fresh chili</div><div class="row desc">cooked in Napoli sauce<span class="lead"></span><span class="price">$15</span></div></div>
    <div class="menu-item"><div class="item-name">Marinara</div><div class="desc">mussels, prawns, calamari, scallops</div><div class="row desc">cooked in Napoli sauce<span class="lead"></span><span class="price">$15</span></div></div>
    <div class="menu-item"><div class="item-name">Risotto Polo</div><div class="row desc">chicken, mushroom, onion, cooked in a cream sauce<span class="lead"></span><span class="price">$16.5</span></div></div>
    <div class="menu-item"><div class="item-name">Lasagna</div><div class="row desc">Homemade Lasagna<span class="lead"></span><span class="price">$15</span></div></div>
    <div class="menu-item"><div class="item-name item-name--red">Pasta Your way</div><div class="row desc">choose any 3 ingredients with cream or Napoli sauce<span class="lead"></span><span class="price">$14.5</span></div></div>
  </div>
</section>

</body>
</html>
```